Bright Path Attorneys Billboard Design for Personal Injury Law Firm

Need a billboard design that we can use for different versions. 1400px X 400px jpeg or png
I have attached the logo and the attorney for the billboard. Attorney Marla Benning
Here is a link to our current website brightpathlegalgroup.example

HEADLINE: HIT BY A TRUCK?
SUBHEAD: NO FEE. BIG FIGHT.
877-GRANTLY

HEADLINE: ACCIDENT?
SUBHEAD: NO FEE, UNLESS WE WIN!
877-GRANTLY

HEADLINE: BIG TRUCK. BIG CASE.
SUBHEAD: YOU PAY $0 UPFRONT
877-GRANTLY

Target Market(s)

People in Car Accident

Industry/Entity Type

Personal Injury Attorneys

```html
<!DOCTYPE html>
<html lang="en">
<head>
<meta charset="utf-8">
<title>Bright Path Attorneys – Big Truck. Big Case.</title>
<link href="https://fonts.googleapis.com/css2?family=Poppins:wght@300;400;600;700;800&display=swap" rel="stylesheet">
<style>
  :root {
    --ink: #0b1216;
    --ink-deep: #070c0f;
    --green: #5fd33e;
    --white: #ffffff;
    --cream: #f4eedf;
    --sky-light: #d8d8d4;
    --sky: #8e918f;
    --earth: #9a7436;
    --earth-dark: #5e4826;
    --road: #2e2e2c;
  }
  * { margin: 0; padding: 0; box-sizing: border-box; }
  html, body { width: 1200px; height: 343px; overflow: hidden; background: var(--ink); }
  .billboard {
    position: relative;
    width: 1200px;
    height: 343px;
    overflow: hidden;
    font-family: "Poppins", sans-serif;
    background:
      radial-gradient(ellipse 120px 240px at 1215px 150px, rgba(95, 211, 62, 0.45), transparent 70%),
      linear-gradient(90deg, var(--ink) 0%, var(--ink-deep) 100%);
  }
  .hero-photo {
    position: absolute;
    left: 0; top: 0;
    width: 620px; height: 343px;
    background:
      radial-gradient(ellipse 130px 60px at 190px 250px, rgba(255, 170, 80, 0.35), transparent 75%),
      linear-gradient(180deg, var(--sky-light) 0%, var(--sky) 28%, var(--earth) 52%, var(--earth-dark) 72%, var(--road) 88%, #242422 100%);
  }
  .hero-fade {
    position: absolute;
    left: 0; top: 0;
    width: 640px; height: 343px;
    background: linear-gradient(90deg, transparent 0%, transparent 55%, rgba(11, 18, 22, 0.7) 78%, var(--ink) 100%);
  }
  .headline {
    position: absolute;
    left: 536px; top: 18px;
    font-weight: 800;
    font-size: 94px;
    line-height: 90px;
    letter-spacing: 0.5px;
    color: var(--white);
    white-space: nowrap;
  }
  .headline .accent { color: var(--green); }
  .subhead {
    position: absolute;
    left: 538px; top: 192px;
    font-weight: 400;
    font-size: 42px;
    line-height: 44px;
    color: var(--cream);
    white-space: nowrap;
  }
  .phone {
    position: absolute;
    left: 538px; top: 255px;
    width: 409px; height: 64px;
    background: var(--green);
    display: flex; align-items: center; justify-content: center;
    font-weight: 700;
    font-size: 45px;
    color: var(--ink-deep);
    letter-spacing: 0.5px;
  }
  .firm-name {
    position: absolute;
    left: 972px; top: 272px;
    display: flex; align-items: center; gap: 10px;
    font-weight: 600;
    font-size: 15px;
    line-height: 17px;
    letter-spacing: 1px;
    text-transform: uppercase;
    color: var(--white);
    white-space: nowrap;
  }
  .firm-name .mark {
    width: 30px; height: 30px;
    background: var(--green);
    flex: none;
  }
</style>
</head>
<body>
  <div class="billboard">
    <div class="hero-photo" role="img" aria-label="Semi truck driving toward the viewer on a desert highway under a cloudy sky"></div>
    <div class="hero-fade"></div>

    <h1 class="headline">
      <span class="accent">BIG</span> TRUCK.<br>
      BIG <span class="accent">CASE.</span>
    </h1>
    <p class="subhead">YOU PAY $0 UPFRONT</p>
    <div class="phone">877-GRANTLY</div>
    <div class="firm-name"><span class="mark"></span><span>Bright Path<br>Attorneys</span></div>
  </div>
</body>
</html>
```